Fantasy Sports Website re-Design

We need a website designed for our fantasy sports website. The website is TorvexPlay.com . An example of the website layout would be like : https://www.quandrel.com/fantasy-sports/fantasy-sports-solutions. We like this site, because of the screenshots on 1 side and a description on the other side. This layout style will showcase the features we have on our site. Somewhere in the header there will be a video explaining what the site is. We would like the style to be black and gold. Like a casino. Attached is an example logo to give the style we want.

Target Market(s)

fantasy sports

Number of Pages Required

3 page

Colors
fecb35
000000

Requirements
Must have
• mockups of index page
Nice to have
• mockups of sub pages

```html
<!DOCTYPE html>
<html lang="en">
<head>
<meta charset="utf-8">
<title>Torvex Play — Crypto Fantasy Sports</title>
<link href="https://fonts.googleapis.com/css2?family=Montserrat:wght@300;400;600;700;800;900&family=Catamaran:wght@500&display=swap" rel="stylesheet">
<style>
  :root {
    --gold: #fecb35;
    --black: #000000;
    --ink: #2b2b2b;
    --text: #3d3d3d;
    --muted: #6a6a6a;
    --white: #ffffff;
  }
  * { box-sizing: border-box; margin: 0; padding: 0; }
  html, body { width: 1200px; height: 1200px; overflow: hidden; background: var(--white); }
  body { font-family: "Montserrat", sans-serif; position: relative; }

  .site-nav {
    position: absolute; top: 0; left: 0; width: 1200px; height: 58px;
    background: var(--black); display: flex; align-items: center; z-index: 2;
  }
  .brand {
    position: absolute; left: 150px; width: 145px; color: var(--gold);
    font-weight: 700; font-size: 18px; letter-spacing: 0.3px; white-space: nowrap;
  }
  .nav-links { position: absolute; left: 323px; display: flex; gap: 26px; list-style: none; }
  .nav-links li { color: var(--white); font-weight: 600; font-size: 11px; white-space: nowrap; }
  .nav-auth { position: absolute; right: 150px; display: flex; align-items: center; gap: 12px; }
  .nav-login { color: var(--white); font-size: 12px; }
  .btn {
    background: var(--gold); color: var(--white); font-weight: 700; border-radius: 3px;
    display: inline-flex; align-items: center; justify-content: center;
  }
  .nav-signup { width: 75px; height: 34px; font-size: 12px; }

  .hero {
    position: absolute; top: 58px; left: 0; width: 1200px; height: 522px;
    background:
      radial-gradient(ellipse at 78% 30%, #4a4a4a 0%, #2e2e2e 40%, #1e1e1e 75%),
      #222;
  }
  .hero-title {
    position: absolute; left: 150px; top: 76px; color: var(--white);
    font-weight: 900; font-size: 41.5px; line-height: 54px; letter-spacing: 0.2px;
  }
  .hero-motto {
    position: absolute; left: 150px; top: 176px; color: var(--gold);
    font-size: 15px; letter-spacing: 3.3px; font-weight: 400; white-space: nowrap;
  }
  .hero-lead {
    position: absolute; left: 150px; top: 206px; width: 340px; color: var(--gold);
    font-family: "Catamaran", sans-serif; font-weight: 500; font-size: 16.5px; line-height: 25px;
  }
  .video {
    position: absolute; left: 650px; top: 166px; width: 400px; height: 259px;
    background: linear-gradient(180deg, #cfd4d6 0%, #b9bdbc 45%, #6f8d55 75%, #5e7a48 100%);
    box-shadow: 0 6px 18px rgba(0,0,0,.5); overflow: hidden;
  }

  .steps {
    position: absolute; top: 580px; left: 0; width: 1200px; height: 166px;
    background: var(--gold); box-shadow: 0 2px 4px rgba(0,0,0,.15);
  }
  .step { position: absolute; top: 14px; width: 200px; text-align: center; }
  .step svg { display: block; margin: 0 auto; width: 80px; height: 86px; }
  .step-label {
    margin-top: 14px; color: var(--ink); font-weight: 700; font-size: 16px; line-height: 20px;
  }
  .step-label.spaced { letter-spacing: 2px; font-size: 16.5px; }

  .about { position: absolute; top: 746px; left: 0; width: 1200px; text-align: center; }
  .about-title {
    margin-top: 64px; color: var(--ink); font-weight: 700; font-size: 37px; line-height: 44px;
  }
  .about-rule { width: 80px; height: 3px; background: var(--gold); margin: 7px auto 0; }
  .about-copy {
    width: 900px; margin: 38px auto 0; color: var(--text);
    font-weight: 300; font-size: 19.2px; line-height: 30px;
  }
  .about-cta { margin-top: 13px; width: 164px; height: 41px; font-size: 13px; }
  .about-note { margin-top: 13px; color: var(--muted); font-size: 13px; font-weight: 300; }
</style>
</head>
<body>
  <header class="site-nav">
    <div class="brand">TORVEX PLAY</div>
    <ul class="nav-links">
      <li>FANTASY</li><li>LOBBY</li><li>STATISTICS</li><li>REFERRAL</li><li>MOBILE APP</li><li>GAME TYPES</li>
    </ul>
    <div class="nav-auth">
      <span class="nav-login">Log In</span>
      <span class="btn nav-signup">Sign Up</span>
    </div>
  </header>

  <section class="hero" role="img" aria-label="Dark blurred photo of a football player in helmet and gloves">
    <h1 class="hero-title">THE LEADER IN CRYPTO<br>FANTASY SPORTS</h1>
    <p class="hero-motto">“our partners’ success is our success”</p>
    <p class="hero-lead">Think you know sports? Play against users from all over the world</p>

    <div class="video" role="img" aria-label="Explainer video still of a sprinter in starting position on a field">
      <svg width="400" height="259" viewBox="0 0 400 259">
        <circle cx="200" cy="110" r="59" fill="rgba(255,255,255,.18)" stroke="rgba(255,255,255,.75)" stroke-width="3"/>
        <path d="M186 86 L222 110 L186 134 Z" fill="rgba(255,255,255,.8)"/>
        <rect x="0" y="219" width="400" height="40" fill="rgba(0,0,0,.75)"/>
        <path d="M15 233 L24 239 L15 245 Z" fill="#bbb"/>
        <rect x="36" y="238" width="312" height="2" fill="#555"/>
        <rect x="36" y="237" width="34" height="3" fill="var(--gold)"/>
        <circle cx="70" cy="238.5" r="3" fill="var(--gold)"/>
        <path d="M308 234 h3 l4 -3 v14 l-4 -3 h-3 z" fill="var(--gold)"/>
        <g fill="var(--gold)"><rect x="324" y="233" width="2" height="11"/><rect x="328" y="233" width="2" height="11"/><rect x="332" y="233" width="2" height="11"/></g>
        <g fill="#777"><rect x="336" y="233" width="2" height="11"/></g>
        <text x="352" y="243" font-family="Montserrat, sans-serif" font-size="9" font-weight="800" font-style="italic" fill="var(--gold)">HD</text>
        <path d="M379 234 h-3 v3 M385 234 h3 v3 M379 244 h-3 v-3 M385 244 h3 v-3" stroke="#888" fill="none" stroke-width="1.2"/>
      </svg>
    </div>
  </section>

  <section class="steps">
    <div class="step" style="left:164px">
      <svg viewBox="0 0 80 86">
        <path d="M4 4 h40 l14 14 v60 a4 4 0 0 1 -4 4 h-50 a4 4 0 0 1 -4 -4 v-70 a4 4 0 0 1 4 -4z" fill="#1f1f1f"/>
        <path d="M44 4 v14 h14" fill="#3a3a3a"/>
        <g stroke="var(--gold)" stroke-width="3" stroke-linecap="round">
          <line x1="12" y1="28" x2="36" y2="28"/><line x1="12" y1="38" x2="40" y2="38"/>
          <line x1="12" y1="48" x2="32" y2="48"/><line x1="12" y1="58" x2="28" y2="58"/><line x1="12" y1="68" x2="30" y2="68"/>
        </g>
        <path d="M70 26 l7 7 -30 30 -10 3 3 -10z" fill="#1f1f1f" stroke="var(--gold)" stroke-width="2.5"/>
      </svg>
      <p class="step-label spaced">Sign Up for FREE</p>
    </div>
    <div class="step" style="left:388px">
      <svg viewBox="0 0 80 86">
        <path d="M40 2 C52 12 64 14 72 14 v30 C72 64 56 78 40 84 C24 78 8 64 8 44 v-30 C16 14 28 12 40 2z" fill="#1f1f1f"/>
        <path d="M28 42 l9 9 16 -18" fill="none" stroke="var(--gold)" stroke-width="5" stroke-linecap="round" stroke-linejoin="round"/>
      </svg>
      <p class="step-label">Add Funds<br>Securely</p>
    </div>
    <div class="step" style="left:612px">
      <svg viewBox="0 0 80 86">
        <path d="M18 16 h44 v16 c0 14 -10 24 -22 24 s-22 -10 -22 -24z" fill="#1f1f1f"/>
        <path d="M18 20 h-12 v6 c0 10 8 16 16 16 M62 20 h12 v6 c0 10 -8 16 -16 16" fill="none" stroke="#1f1f1f" stroke-width="6"/>
        <rect x="35" y="54" width="10" height="14" fill="#1f1f1f"/>
        <rect x="24" y="68" width="32" height="8" fill="#1f1f1f"/>
      </svg>
      <p class="step-label">Choose Contests in<br>the Lobby</p>
    </div>
    <div class="step" style="left:838px">
      <svg viewBox="0 0 80 86">
        <g fill="#1f1f1f">
          <circle cx="16" cy="22" r="11"/><circle cx="64" cy="22" r="11"/>
          <path d="M0 62 c0 -18 6 -26 16 -26 s16 8 16 26z"/><path d="M48 62 c0 -18 6 -26 16 -26 s16 8 16 26z"/>
        </g>
        <circle cx="40" cy="34" r="13" fill="#1f1f1f" stroke="var(--gold)" stroke-width="3"/>
        <path d="M18 80 c0 -22 8 -32 22 -32 s22 10 22 32z" fill="#1f1f1f" stroke="var(--gold)" stroke-width="3"/>
      </svg>
      <p class="step-label">Draft a Team.<br>Enter &amp; Enjoy</p>
    </div>
  </section>

  <section class="about">
    <h2 class="about-title">What is Torvex Play?</h2>
    <div class="about-rule"></div>
    <p class="about-copy">Torvex Play is an exciting Fantasy Sports platform supporting todays Fantasy Sports Crypto currencies. Players can participate in Fantasy Sports contests using crypto currencies to play against other players. Torvex Play has more sports and game types than any other fantasy sports website with more features on the way. Due to the use of todays Fantasy Sports Crypto currencies, Torvex Play has the lowest transaction fees and the most secure platform.</p>
    <span class="btn about-cta">Sign Up Now it’s Free</span>
    <p class="about-note">*Free and Paid games available</p>
  </section>
</body>
</html>
```